Private Medical Clinic needs a letterhead design

Letterhead that can be edited. Letter head is needed for printing official doctor's notes, referrals, etc in a medical clinic. The letterhead should use the attached logos

```html
<!DOCTYPE html>
<html lang="en">
<head>
<meta charset="utf-8">
<title>Tall Birch Family Medicine – Stationery</title>
<link rel="stylesheet" href="https://fonts.googleapis.com/css2?family=EB+Garamond:wght@500&family=Questrial&family=Roboto:wght@400;500&display=swap">
<style>
  :root{
    --backdrop:#dcdcdc;
    --paper-light:#ffffff;
    --paper-shade:#e4e4e4;
    --brand-dark:#464b42;
    --brand-ink:#4a4f47;
    --body-ink:#5a5a5a;
    --footer-ink:#ffffff;
    --sign-ink:#2f5fa8;
  }
  *{box-sizing:border-box;margin:0;padding:0}
  html,body{width:1200px;height:877px;overflow:hidden;background:var(--backdrop)}
  .canvas{position:relative;width:1200px;height:877px}

  .sheet{position:absolute;box-shadow:0 1px 4px rgba(0,0,0,.18);overflow:hidden}

  .brand-name{font-family:"EB Garamond",serif;font-weight:500;color:var(--brand-ink);text-align:center;line-height:1.05;display:flex;align-items:center;gap:6px}
  .brand-dot{width:10px;height:10px;border-radius:50%;background:currentColor;flex:none}

  /* Letterhead */
  .letterhead{left:61px;top:64px;width:527px;height:744px;
    background:linear-gradient(90deg,var(--paper-light) 0%,#f3f3f3 40%,var(--paper-shade) 100%)}
  .letterhead .brand-name{position:absolute;left:0;right:0;top:50px;justify-content:center;font-size:22px}
  .letter-body{position:absolute;left:45px;top:208px;width:440px;font-family:"Questrial",sans-serif;color:var(--body-ink)}
  .greeting{font-size:13px;margin-bottom:25px}
  .letter-body p.para{font-size:7.4px;line-height:11.4px;margin-bottom:11.4px;text-align:left}
  .closing{font-size:7.4px;margin-top:20px}
  .signature{position:absolute;left:41px;top:518px;width:96px;height:44px;
    background:linear-gradient(90deg,rgba(47,95,168,.18),rgba(47,95,168,.06));border-radius:3px}
  .corner-mark{position:absolute;width:12px;height:12px;border-radius:50%;background:var(--brand-ink);opacity:.75}

  .footer-band{position:absolute;left:0;right:0;background:var(--brand-dark);color:var(--footer-ink);
    font-family:"Roboto",sans-serif;font-size:8px;text-align:center}
  .letterhead .footer-band{top:702px;height:42px;padding-top:7px}
  .footer-address{display:inline-block;padding-bottom:2px;border-bottom:1px solid var(--footer-ink)}
  .footer-address strong{font-weight:500}
  .footer-contacts{margin-top:4px;display:flex;justify-content:center;gap:6px;align-items:center}
  .footer-contacts span{display:inline-flex;align-items:center;gap:2px}
  .footer-contacts svg{width:7px;height:7px;fill:var(--footer-ink)}

  /* Envelope back */
  .envelope-back{left:620px;top:294px;width:531px;height:240px;
    background:linear-gradient(90deg,#ffffff 0%,#f1f1f1 100%)}
  .envelope-flap{position:absolute;left:0;top:0;width:531px;height:74px}
  .envelope-back .brand-name{position:absolute;left:0;right:0;top:24px;justify-content:center;color:#ffffff;font-size:15px}

  /* Envelope front */
  .envelope-front{left:620px;top:566px;width:532px;height:242px;
    background:linear-gradient(90deg,#ffffff 0%,#f2f2f2 100%)}
  .envelope-front .brand-name{position:absolute;left:24px;top:38px;font-size:21px;text-align:left}
  .envelope-front .footer-band{top:216px;height:26px;line-height:26px}
  .envelope-front .footer-band strong{font-weight:500}
</style>
</head>
<body>
<main class="canvas">

  <section class="sheet letterhead">
    <div class="brand-name"><span class="brand-dot"></span>Tall Birch Family Medicine</div>

    <div class="letter-body">
      <p class="greeting">Dear Mr. Carter,</p>
      <p class="para">Lorem ipsum dolor sit amet, consectetur adipiscing elit. Donec orci purus, luctus vitae dignissim eu, iaculis sed purus. Vivamus faucibus, ipsum nec aliquet viverra, leo mauris condimentum ligula, sit amet sagittis enim ligula quis arcu. Nam egestas tortor id nisi porttitor mattis. In tortor ante, ultricies in suscipit a, tempus non massa. Vivamus et auctor mi. Fusce vel massa nulla. Phasellus nec eros mauris, et scelerisque orci.</p>
      <p class="para">Donec malesuada orci vitae nulla accumsan porta a id massa. Quisque accumsan iaculis magna sit amet fringilla. Maecenas consequat, magna eget tincidunt semper, odio nibh rutrum mi, id feugiat ante nisi eu risus. Vestibulum nunc orci, rhoncus a placerat in, ultricies in mi. Cras mattis varius eros, vel fringilla nisi suscipit eget. Quisque scelerisque sagittis nulla at porttitor.</p>
      <p class="para">Sed id augue vitae urna euismod commodo aliquet a quam. Pellentesque arcu velit, cursus et malesuada ut, consequat et diam. Nullam erat sem, rhoncus id ullamcorper vitae, rhoncus et arcu. In ultricies ultricies nulla, ut rutrum nisi iaculis at. Donec eu magna a metus ornare faucibus. Fusce aliquet faucibus ultricies. Morbi semper, est id tincidunt gravida, sem arcu adipiscing lacus, ac bibendum nulla leo eu purus. Quisque nec diam sed risus consectetur a ccumsan quis quis nibh. Vestibulum id purus lorem.</p>
      <p class="para">It is a long established fact that a reader will be distracted by the readable content of a page when looking at its layout. The point of using Lorem Ipsum is that it has a more-or-less normal distribution of letters, as opposed to using 'Content here, content here', making it look like readable English. Many desktop publishing packages</p>
      <p class="closing">Sincerely,</p>
    </div>

    <div class="signature" role="img" aria-label="Handwritten signature of Paul Carter"></div>
    <span class="corner-mark" style="left:490px;top:676px"></span>

    <footer class="footer-band">
      <div class="footer-address"><strong>Tall Birch Family Medicine</strong> | 218 Aspen Row, Juneau, Alaska 99801</div>
      <div class="footer-contacts">
        <span><svg viewBox="0 0 10 10"><path d="M2 0.5 3.8 2.6 2.9 3.9Q4 6.2 6.1 7.1L7.4 6.2 9.5 8 8.4 9.5Q4.6 9.6 1.9 6.4 0.1 4 0.6 1.6Z"/></svg>555-014-2287</span>
        <span><svg viewBox="0 0 10 10"><path d="M0 2h10v6H0z M0.8 2.6 5 5.6 9.2 2.6" stroke="#464b42" stroke-width=".8"/></svg>hello@tallbirchclinic.com</span>
        <span><svg viewBox="0 0 10 10"><circle cx="5" cy="5" r="4.5"/></svg>www.tallbirchclinic.com</span>
      </div>
    </footer>
  </section>

  <section class="sheet envelope-back">
    <svg class="envelope-flap" viewBox="0 0 531 74" aria-hidden="true">
      <path d="M0 0H531L524 30Q517 74 490 74H41Q14 74 7 30Z" fill="var(--brand-dark)"/>
    </svg>
    <div class="brand-name"><span class="brand-dot"></span>Tall Birch Family Medicine</div>
  </section>

  <section class="sheet envelope-front">
    <div class="brand-name"><span class="brand-dot"></span>Tall Birch Family Medicine</div>
    <span class="corner-mark" style="left:489px;top:190px"></span>
    <footer class="footer-band"><strong>Tall Birch Family Medicine</strong> | 218 Aspen Row, Juneau, Alaska 99801</footer>
  </section>

</main>
</body>
</html>
```